Business card with professional look

I would like a creative yet professional looking business card for our business. We sell broadcast TV related security products for mobile phones, set top boxes, and tablets. Our customers are international. We have a logo we like and I would like to possibly add some color to the business card but keep it professional looking.

Target Market(s)

Professionals in the TV, cable, ans Satellite industries

Industry/Entity Type

Cable Tv

Contact Information for Business Card

Name Tom Verhanic, title CEO, Address 8160 Marbury Crescent, Suite 300, Ferndale Point, CA 91584 USA, phone numbers m:+1.619.472.3014 o:+1.855.263.9042, email, logo

Font styles to use
Other font styles liked:
• Open to any font that looks good with logo

Requirements
Must have
• professional look with colors coordinated with logo colors. would like to add one or two different colors as well as some form of background color

```html
<!DOCTYPE html>
<html lang="en">
<head>
<meta charset="utf-8">
<title>Veilcast Business Card</title>
<link href="https://fonts.googleapis.com/css2?family=Lato:wght@400;700;900&display=swap" rel="stylesheet">
<style>
  :root {
    --backdrop: #3b3b3c;
    --card: #ffffff;
    --panel: #e9ecf7;
    --ink: #2b2b2b;
    --muted: #6d6d72;
    --rule: #4a4a4a;
    --brand-blue: #1c5cae;
    --bright-blue: #2f93d9;
    --charcoal: #333335;
  }
  * { box-sizing: border-box; margin: 0; padding: 0; }
  html, body { width: 1200px; height: 810px; overflow: hidden; }
  body {
    background: var(--backdrop);
    font-family: "Lato", sans-serif;
    position: relative;
  }
  .business-card {
    position: absolute;
    left: 100px; top: 135px;
    width: 1000px; height: 540px;
    background: var(--card);
    overflow: hidden;
  }
  .card-art { position: absolute; inset: 0; width: 100%; height: 100%; }
  .brand-name {
    position: absolute;
    left: 110px; top: 150px;
    font-size: 66px;
    font-weight: 900;
    letter-spacing: -1px;
    color: var(--charcoal);
    display: flex; align-items: center; gap: 16px;
  }
  .brand-mark {
    width: 22px; height: 22px;
    background: var(--brand-blue);
    border-radius: 50%;
  }
  .identity {
    position: absolute;
    right: 70px; top: 110px;
    text-align: right;
  }
  .person-name {
    font-size: 30px;
    font-weight: 400;
    color: var(--brand-blue);
  }
  .person-title {
    font-size: 17px;
    color: var(--muted);
    letter-spacing: 1px;
    border-bottom: 1.5px solid var(--muted);
    padding-bottom: 3px;
    margin-left: 120px;
  }
  .address {
    margin-top: 18px;
    font-size: 19px;
    line-height: 1.4;
    color: var(--ink);
  }
  .contact-list {
    position: absolute;
    left: 72px; top: 402px;
    list-style: none;
    font-size: 20px;
    line-height: 1.35;
    color: var(--ink);
  }
  .contact-list li { display: flex; align-items: center; gap: 8px; }
  .contact-list svg { width: 16px; height: 16px; fill: var(--brand-blue); flex: none; }
</style>
</head>
<body>
  <article class="business-card">
    <svg class="card-art" viewBox="0 0 1000 540" aria-hidden="true">
      <rect class="info-panel" x="560" y="55" width="440" height="330" fill="var(--panel)"/>
      <line class="divider" x1="0" y1="385" x2="1000" y2="385" stroke="var(--rule)" stroke-width="1.2"/>
      <polygon class="ribbon-blue" points="650,450 700,390 1000,390 1000,446 680,446 662,466" fill="var(--brand-blue)"/>
      <polygon class="ribbon-charcoal" points="0,496 626,496 666,452 684,452 636,510 0,510" fill="var(--charcoal)"/>
      <polyline class="accent-line" points="0,520 642,520 692,458 1000,458" fill="none" stroke="var(--bright-blue)" stroke-width="4"/>
    </svg>

    <div class="brand-name"><span>Veilcast</span><span class="brand-mark"></span></div>

    <div class="identity">
      <p class="person-name">Tom Verhanic</p>
      <p class="person-title">CEO</p>
      <p class="address">8160 Marbury Crescent<br>Suite 300<br>Ferndale Point, CA 91584 USA</p>
    </div>

    <ul class="contact-list">
      <li><svg viewBox="0 0 16 16"><path d="M3 1l3 3-1.5 2c1 2 3 4 5 5L11.5 9.5l3 3-2 2.5C6 14 2 10 1 3z"/></svg>+1.619.472.3014</li>
      <li><svg viewBox="0 0 16 16"><path d="M4 0h8a1 1 0 0 1 1 1v14a1 1 0 0 1-1 1H4a1 1 0 0 1-1-1V1a1 1 0 0 1 1-1zm1 2v10h6V2zm3 11a1 1 0 1 0 0 2 1 1 0 0 0 0-2z"/></svg>+1.855.263.9042</li>
      <li><svg viewBox="0 0 16 16"><path d="M0 3h16v1L8 9 0 4zm0 3l8 5 8-5v7H0z"/></svg>info@veilcast.com</li>
    </ul>
  </article>
</body>
</html>
```